・ターゲット
美容室は銀座にあり、客層は20代~50代の女性です。
メインターゲットは30代です。

・サイトの色
白がベースでブラック、グレーで洗練された
透明感を表現してください。

「シンプルで美しく、魅力的なデザインでかつ予約導線がよいサイト」
を目指しています。

ラフデザイン案がありますので、
レイアウトは基本的にラフデザインをベースにしていただき、
ユーザビリティ的によりよくなる提案があれば理由とともに
アレンジしてください。

ロゴ、使用素材はお渡しします。
1ページ
白、グレー、黒
• フォトショップ形式 (.psd)
• PNG形式 (.png)
提案数が想定よりも少ないため延長させていただきます。参加報酬も4件に増やさせていただきました。
たくさんのご応募ありがとうございます。
トップの表記では選定期限が1/31までとなっておりますが、
現在、最終選定期限を2/5になっております。

期限までには当選対象者にご連絡できるかと思いますのでよろしくお願いします。
現在、候補のランサー様に修正依頼を投げています。
最終選定期限を再度、延長していただいています。

長くなってしまい申し訳ございませんが今しばらくお待ちください。

素材の魅力を最大限に引き出していただけたところが、クライアントに気に入っていただけたポイントでした。ありがとうございます。

たくさんのご提案ありがとうございました。

言葉足らずの点もあったと思いますが、言語外の意図を読み取っていただけて、これほど多様なデザインの提案をいただけるとは思っていませんでした。

たくさんの中から絞り込むのはとても大変な作業で、時間もかかってしまい申し訳ありませんでした。お選びできなかった皆様に申し訳ない気持ちでいっぱいです。
また、このような機会がありましたら、何卒よろしくお願いいたします。

```html
<!DOCTYPE html>
<html lang="ja">
<head>
<meta charset="utf-8">
<title>Salon | 銀座ヘアサロン</title>
<link rel="stylesheet" href="https://fonts.googleapis.com/css2?family=Cormorant+Garamond:wght@500;600&family=Noto+Sans+JP:wght@400;500;700&family=Noto+Serif+JP:wght@400;600&display=swap">
<style>
:root{
  --ink:#111111;
  --ink-soft:#2b2b2b;
  --gray:#8a8a8a;
  --gray-line:#d6d6d6;
  --gray-pale:#efefef;
  --paper:#ffffff;
  --gold:#b39a4f;
}
*{box-sizing:border-box;margin:0;padding:0}
html,body{width:1200px;height:5032px;overflow:hidden;background:var(--paper)}
body{font-family:"Noto Sans JP",sans-serif;color:var(--ink);position:relative}
.abs{position:absolute}

/* hero */
.hero{left:0;top:0;width:1200px;height:712px;background:
  radial-gradient(ellipse 300px 360px at 700px 330px,rgba(60,45,35,.55),rgba(60,45,35,0) 70%),
  radial-gradient(ellipse 420px 520px at 640px 300px,#cfc6bd 0%,rgba(207,198,189,0) 70%),
  linear-gradient(100deg,#f2f2f2 0%,#c9c9c9 30%,#7c7772 55%,#b8b3ad 75%,#e8e8e8 100%)}
.hero-logo{left:112px;top:56px;color:var(--paper);font-family:"Cormorant Garamond",serif;font-size:40px;font-weight:600;display:flex;align-items:center;gap:12px}
.hero-logo i{display:block;width:22px;height:22px;background:var(--paper)}
.hero-next{right:72px;top:320px}
.hero-tag{left:112px;top:450px}
.hero-tag span{display:block;background:var(--ink);color:var(--paper);font-family:"Cormorant Garamond",serif;font-size:22px;letter-spacing:3px;padding:4px 18px;margin-bottom:8px;width:max-content}

.gnav{left:88px;top:620px;width:1072px;height:92px;display:flex;background:rgba(238,238,238,.96)}
.gnav a{flex:1;text-align:center;color:var(--ink-soft);border-right:1px solid var(--gray-line);padding-top:20px;white-space:nowrap}
.gnav a:nth-child(6){flex:1.35}
.gnav a:nth-child(7){flex:1.35}
.gnav a:last-child{border-right:0}
.gnav a.on{background:#8c8c8c;color:var(--paper)}
.gnav b{display:block;font-family:"Cormorant Garamond",serif;font-size:23px;letter-spacing:2px;font-weight:600}
.gnav small{font-size:11px}

.brand{left:0;top:740px;width:1200px;text-align:center;font-family:"Cormorant Garamond",serif;font-weight:600;font-size:44px;color:var(--gold)}
.brand i{display:block;width:26px;height:26px;background:var(--gold);margin:0 auto 6px}

/* intro */
.intro{left:120px;top:900px;width:980px;height:640px;background:
  radial-gradient(ellipse 220px 300px at 490px 560px,#d9a35a 0%,rgba(217,163,90,0) 70%),
  radial-gradient(ellipse at 50% 85%,#8a5a2a 0%,#3a2414 45%,#0e0a07 100%)}
.intro-copy{left:120px;top:940px;width:980px;text-align:center;color:var(--paper);font-family:"Noto Serif JP",serif;font-size:17px;line-height:36px;letter-spacing:1px}

.reserve{left:240px;top:1552px;width:720px;height:68px;background:var(--gold);color:var(--paper);font-size:28px;letter-spacing:6px;display:flex;align-items:center;justify-content:center;font-weight:500}
.tel{left:0;top:1630px;width:1200px;text-align:center;font-size:22px;letter-spacing:3px;color:var(--ink-soft)}
.tel small{display:block;font-size:13px;letter-spacing:1px;color:var(--gray);margin-top:2px}

/* catalog */
.catalog{left:152px;top:1760px;width:896px;display:grid;grid-template-columns:repeat(4,200px);column-gap:32px;row-gap:28px}
.style-card .photo{height:210px}
.style-card h3{font-size:15px;font-weight:500;margin-top:10px}
.style-card p{font-size:12px;line-height:18px;color:var(--gray);margin-top:4px}
.tone-a{background:radial-gradient(ellipse 70px 90px at 50% 42%,#e8d2c2,rgba(232,210,194,0) 75%),radial-gradient(ellipse 95px 120px at 50% 45%,#7a5a44,rgba(122,90,68,0) 80%),linear-gradient(180deg,#9b9b9b,#d0d0d0)}
.tone-b{background:radial-gradient(ellipse 65px 85px at 52% 40%,#f0dccd,rgba(240,220,205,0) 75%),radial-gradient(ellipse 100px 130px at 50% 48%,#4b3428,rgba(75,52,40,0) 80%),linear-gradient(180deg,#f3f3f3,#e2e2e2)}
.tone-c{background:radial-gradient(ellipse 65px 85px at 48% 42%,#ead4c3,rgba(234,212,195,0) 75%),radial-gradient(ellipse 95px 125px at 50% 46%,#2e221c,rgba(46,34,28,0) 80%),linear-gradient(180deg,#fafafa,#e8e8e8)}
.tone-d{background:radial-gradient(ellipse 65px 80px at 50% 44%,#f2e0d0,rgba(242,224,208,0) 75%),radial-gradient(ellipse 100px 110px at 50% 44%,#d8bf8c,rgba(216,191,140,0) 80%),linear-gradient(180deg,#f5f5f5,#e6e6e6)}
.tone-e{background:radial-gradient(ellipse 65px 85px at 50% 42%,#eed7c6,rgba(238,215,198,0) 75%),radial-gradient(ellipse 90px 115px at 50% 45%,#8c6a4e,rgba(140,106,78,0) 80%),linear-gradient(180deg,#f6f6f6,#e4e4e4)}
.tone-f{background:radial-gradient(ellipse 60px 85px at 50% 40%,#ecd4c2,rgba(236,212,194,0) 75%),radial-gradient(ellipse 100px 140px at 50% 50%,#241a15,rgba(36,26,21,0) 80%),linear-gradient(180deg,#f4f4f4,#e2e2e2)}
.tone-g{background:radial-gradient(ellipse 65px 85px at 50% 42%,#e9d1bf,rgba(233,209,191,0) 75%),radial-gradient(ellipse 100px 120px at 50% 46%,#1e1a1c,rgba(30,26,28,0) 80%),linear-gradient(180deg,#dfe6ec,#c4ccd4)}
.tone-h{background:radial-gradient(ellipse 65px 85px at 50% 42%,#f0dccb,rgba(240,220,203,0) 75%),radial-gradient(ellipse 100px 115px at 50% 45%,#a68158,rgba(166,129,88,0) 80%),linear-gradient(180deg,#f5f5f5,#e4e4e4)}
.more{left:780px;top:2416px;font-family:"Cormorant Garamond",serif;font-size:32px;font-weight:600;display:flex;align-items:center;gap:10px}
.more-btn{left:780px;top:2474px;width:280px;height:30px;background:var(--gold);color:var(--paper);font-size:13px;letter-spacing:3px;display:flex;align-items:center;justify-content:center}

/* stylist */
.side-bar{left:0;top:2560px;width:30px;height:640px;background:var(--ink)}
.sec-title{font-family:"Cormorant Garamond",serif;font-weight:600;font-size:46px;display:flex;align-items:center;gap:12px}
.sec-title i{display:block;width:28px;height:28px;background:var(--ink)}
.sec-title small{font-family:"Noto Sans JP",sans-serif;font-size:14px;font-weight:400;color:var(--gray);margin-left:6px}
.stylists{left:120px;top:2730px;width:940px;display:grid;grid-template-columns:repeat(5,176px);column-gap:15px;row-gap:26px}
.stylist .photo{height:206px}
.stylist p{text-align:center;font-size:14px;margin-top:8px}
.p1{background:radial-gradient(ellipse 45px 60px at 50% 38%,#d9b8a0,rgba(217,184,160,0) 75%),radial-gradient(ellipse 90px 70px at 50% 100%,#2a2a2a,rgba(42,42,42,0) 85%),linear-gradient(180deg,#6f6f6f,#4a4a4a)}
.p2{background:radial-gradient(ellipse 45px 60px at 50% 38%,#ecd2bf,rgba(236,210,191,0) 75%),radial-gradient(ellipse 75px 110px at 50% 42%,#3a2a22,rgba(58,42,34,0) 80%),radial-gradient(ellipse 90px 70px at 50% 100%,#1d1d1d,rgba(29,29,29,0) 85%),linear-gradient(180deg,#f0f0f0,#d8d8d8)}
.p3{background:radial-gradient(ellipse 45px 60px at 50% 38%,#e6c7ae,rgba(230,199,174,0) 75%),radial-gradient(ellipse 90px 70px at 50% 100%,#ffffff,rgba(255,255,255,0) 85%),linear-gradient(180deg,#b58a4e,#8f6b3c)}
.p4{background:radial-gradient(ellipse 45px 60px at 50% 40%,#efd6c4,rgba(239,214,196,0) 75%),radial-gradient(ellipse 80px 100px at 50% 38%,#a47a4e,rgba(164,122,78,0) 80%),radial-gradient(ellipse 90px 70px at 50% 100%,#f5f5f5,rgba(245,245,245,0) 85%),linear-gradient(180deg,#d9d9d9,#c2c2c2)}
.p5{background:radial-gradient(ellipse 45px 60px at 50% 38%,#e3c2a8,rgba(227,194,168,0) 75%),radial-gradient(ellipse 90px 70px at 50% 100%,#2d3c66,rgba(45,60,102,0) 85%),linear-gradient(180deg,#ededed,#d7d7d7)}
.p6{background:radial-gradient(ellipse 45px 60px at 50% 38%,#e8cdb8,rgba(232,205,184,0) 75%),radial-gradient(ellipse 90px 70px at 50% 100%,#e8e8e8,rgba(232,232,232,0) 85%),linear-gradient(180deg,#e0e0e0,#c6c6c6)}
.p7{background:radial-gradient(ellipse 45px 60px at 50% 40%,#e4c6ae,rgba(228,198,174,0) 75%),radial-gradient(ellipse 80px 95px at 50% 36%,#2a2019,rgba(42,32,25,0) 80%),radial-gradient(ellipse 90px 70px at 50% 100%,#1a1a1a,rgba(26,26,26,0) 85%),linear-gradient(180deg,#f2f2f2,#dcdcdc)}
.p8{background:radial-gradient(ellipse 45px 60px at 50% 38%,#eacbb3,rgba(234,203,179,0) 75%),radial-gradient(ellipse 90px 70px at 50% 100%,#e3a9b8,rgba(227,169,184,0) 85%),linear-gradient(180deg,#f4f4f4,#dedede)}
.p9{background:radial-gradient(ellipse 45px 60px at 50% 38%,#ecd0ba,rgba(236,208,186,0) 75%),radial-gradient(ellipse 90px 70px at 50% 100%,#6e6458,rgba(110,100,88,0) 85%),linear-gradient(180deg,#bfb7ad,#9d958c)}
.p10{background:radial-gradient(ellipse 45px 60px at 50% 38%,#e6c6ad,rgba(230,198,173,0) 75%),radial-gradient(ellipse 90px 70px at 50% 100%,#56627a,rgba(86,98,122,0) 85%),linear-gradient(180deg,#f5f5f5,#e0e0e0)}

.interior{left:0;top:3288px;width:1200px;height:544px;background:
  radial-gradient(ellipse 260px 120px at 600px 420px,#ffffff,rgba(255,255,255,0) 75%),
  linear-gradient(90deg,rgba(30,30,30,.55) 0%,rgba(30,30,30,0) 14%,rgba(30,30,30,0) 86%,rgba(30,30,30,.55) 100%),
  linear-gradient(180deg,#fdfdfd 0%,#ececec 30%,#9a9a9a 48%,#e4e4e4 60%,#f7f7f7 100%)}

/* special */
.special{left:120px;top:3900px;width:460px}
.list-title{font-size:18px;font-weight:700;margin:34px 0 10px}
.news li{list-style:none;display:flex;gap:24px;font-size:14px;line-height:30px;border-bottom:1px dotted var(--gray-line)}
.news time{color:var(--gray);width:80px;flex:none}
.social{left:610px;top:3940px;width:450px}
.social h3{font-size:18px;font-weight:700;letter-spacing:1px;padding-bottom:8px;border-bottom:2px solid var(--ink)}
.social-box{border:1px solid var(--gray-line);margin-top:14px;padding:18px;height:420px}
.page-head{display:flex;gap:12px;align-items:center;padding-bottom:14px;border-bottom:1px solid var(--gray-line)}
.page-head i{width:50px;height:50px;background:var(--ink)}
.page-head b{font-size:15px}
.page-head small{display:block;font-size:12px;color:var(--gray)}
.post{font-size:12px;line-height:20px;color:var(--ink-soft);margin:12px 0}
.post-photo{height:200px;background:radial-gradient(ellipse 90px 100px at 30% 60%,#3a3a3a,rgba(58,58,58,0) 80%),linear-gradient(120deg,#d9d4cc,#a39a8e 60%,#7d756b)}

/* footer */
.footer{left:0;top:4480px;width:1200px;height:552px;background:var(--ink);color:var(--paper)}
.footer h2{position:absolute;left:0;top:40px;width:1200px;text-align:center;font-family:"Cormorant Garamond",serif;font-weight:500;font-size:44px;letter-spacing:4px}
.f-info{left:140px;top:140px;width:480px;font-size:14px;line-height:26px}
.f-info h4{font-size:15px;margin-top:18px}
.f-info table td{padding-right:40px}
.f-btns{left:640px;top:140px;width:300px}
.f-btns span{display:block;height:36px;margin-bottom:14px;background:#2a2a2a;border:1px solid #555;text-align:center;line-height:34px;font-size:13px;letter-spacing:2px}
.f-btns span.gold{background:var(--gold);border-color:var(--gold)}
.f-logo{right:80px;top:420px;color:var(--gold);font-family:"Cormorant Garamond",serif;font-weight:600;font-size:38px;text-align:center}
.f-logo i{display:block;width:22px;height:22px;background:var(--gold);margin:0 auto 4px}
.f-bottom{left:0;top:520px;width:1200px;height:32px;background:#000;display:flex;align-items:center;justify-content:center;gap:30px;font-size:11px;color:#999}
</style>
</head>
<body>

<section class="abs hero" role="img" aria-label="Fashion hair photo of a model with long wavy hair"></section>
<div class="abs hero-logo"><i></i>Salon</div>
<svg class="abs hero-next" width="40" height="70" viewBox="0 0 40 70"><polyline points="6,4 34,35 6,66" fill="none" stroke="#fff" stroke-width="4"/></svg>
<div class="abs hero-tag"><span>2015S/W COLLECTION</span><span>HAIR CATALOG</span></div>

<nav class="abs gnav">
  <a class="on"><b>HOME</b><small>ホーム</small></a>
  <a><b>STYLIST</b><small>スタイリスト</small></a>
  <a><b>CATALOG</b><small>カタログ</small></a>
  <a><b>ACCESS</b><small>アクセス</small></a>
  <a><b>PRICE</b><small>料金</small></a>
  <a><b>INFORMATION</b><small>インフォメーション</small></a>
  <a><b>RESERVATION</b><small>予約</small></a>
</nav>

<div class="abs brand"><i></i>Salon</div>

<div class="abs intro" role="img" aria-label="Warmly lit salon entrance lobby"></div>
<div class="abs intro-copy">
  <p>Salon へようこそ！</p>
  <p>Salon の日本は、ヨーロッパの美容企業が長い時をかけた生まれた「サロン」に由来しています。</p>
  <p>ホテルのようなレセプション、自然光あふれる落ち着いたフロア。</p>
  <p>アルフレッドベッドのシャンプー、ブースなどで構成された非日常な空間で、</p>
  <p>最高のカットテクニックとおもてなしを提供します。</p>
  <p>最新トレンドを常に意識し、ゲストそれぞれのライフスタイルに合わせたスタイルをご提案しております。</p>
  <p>今までにない満足感を目指し銀座にオープンしてからも常に進化を続けています。</p>
  <p>これからもゲストの皆様が安心して通っていただけるように、</p>
  <p>スタッフ一同心をこめてお迎えいたします。</p>
  <p>ゲストの皆様が新しい自分に出会えるお手伝いをさせてください。</p>
</div>

<div class="abs reserve">オンライン予約</div>
<div class="abs tel">電話予約　03-0000-1234<small>月・金 11:00-21:00　土 10:00-20:00　日祝 10:00-19:00</small></div>

<section class="abs catalog">
  <article class="style-card"><div class="photo tone-a" role="img" aria-label="Hairstyle photo"></div><h3>ナチュラルウェーブ</h3><p>柔らかな動きで女性らしいシルエットに仕上げます。</p></article>
  <article class="style-card"><div class="photo tone-b" role="img" aria-label="Hairstyle photo"></div><h3>ナチュラルウェーブ</h3><p>柔らかな動きで女性らしいシルエットに仕上げます。</p></article>
  <article class="style-card"><div class="photo tone-c" role="img" aria-label="Hairstyle photo"></div><h3>ナチュラルウェーブ</h3><p>柔らかな動きで女性らしいシルエットに仕上げます。</p></article>
  <article class="style-card"><div class="photo tone-d" role="img" aria-label="Hairstyle photo"></div><h3>ナチュラルウェーブ</h3><p>柔らかな動きで女性らしいシルエットに仕上げます。</p></article>
  <article class="style-card"><div class="photo tone-e" role="img" aria-label="Hairstyle photo"></div><h3>ナチュラルウェーブ</h3><p>柔らかな動きで女性らしいシルエットに仕上げます。</p></article>
  <article class="style-card"><div class="photo tone-f" role="img" aria-label="Hairstyle photo"></div><h3>ナチュラルウェーブ</h3><p>柔らかな動きで女性らしいシルエットに仕上げます。</p></article>
  <article class="style-card"><div class="photo tone-g" role="img" aria-label="Hairstyle photo"></div><h3>ナチュラルウェーブ</h3><p>柔らかな動きで女性らしいシルエットに仕上げます。</p></article>
  <article class="style-card"><div class="photo tone-h" role="img" aria-label="Hairstyle photo"></div><h3>ナチュラルウェーブ</h3><p>柔らかな動きで女性らしいシルエットに仕上げます。</p></article>
</section>
<div class="abs more"><svg width="18" height="20" viewBox="0 0 18 20"><polygon points="0,0 18,10 0,20" fill="#111"/></svg>more style</div>
<div class="abs more-btn">オンライン予約</div>

<div class="abs side-bar"></div>
<h2 class="abs sec-title" style="left:120px;top:2650px"><i></i>Stylist</h2>
<section class="abs stylists">
  <div class="stylist"><div class="photo p1" role="img" aria-label="Stylist portrait"></div><p>代表 高橋 涼</p></div>
  <div class="stylist"><div class="photo p2" role="img" aria-label="Stylist portrait"></div><p>中村 さやか</p></div>
  <div class="stylist"><div class="photo p3" role="img" aria-label="Stylist portrait"></div><p>藤原 和也</p></div>
  <div class="stylist"><div class="photo p4" role="img" aria-label="Stylist portrait"></div><p>森 美奈</p></div>
  <div class="stylist"><div class="photo p5" role="img" aria-label="Stylist portrait"></div><p>吉田 誠司</p></div>
  <div class="stylist"><div class="photo p6" role="img" aria-label="Stylist portrait"></div><p>橋本 一樹</p></div>
  <div class="stylist"><div class="photo p7" role="img" aria-label="Stylist portrait"></div><p>篠田 亮</p></div>
  <div class="stylist"><div class="photo p8" role="img" aria-label="Stylist portrait"></div><p>野口 大輝</p></div>
  <div class="stylist"><div class="photo p9" role="img" aria-label="Stylist portrait"></div><p>前田 ゆりこ</p></div>
  <div class="stylist"><div class="photo p10" role="img" aria-label="Stylist portrait"></div><p>岡田 悠</p></div>
</section>

<div class="abs interior" role="img" aria-label="Bright white salon floor with black styling chairs"></div>

<section class="abs special">
  <h2 class="sec-title"><i></i>Special<small>注目情報</small></h2>
  <h3 class="list-title">RANKING 人気商品ランキング</h3>
  <ul class="news">
    <li><time>2014.1.6</time>冬期シャンプーランキングを更新しました</li>
    <li><time>2014.1.10</time>乾燥肌にぴったりのトリートメントが入荷</li>
    <li><time>2014.1.15</time>etc...</li>
    <li><time>2014.1.19</time>etc...</li>
  </ul>
  <h3 class="list-title">INFORMATION</h3>
  <ul class="news">
    <li><time>2014.1.6</time>◎◎◎新発売されました！</li>
    <li><time>2014.1.10</time>年末年始の営業時間のお知らせ</li>
    <li><time>2014.1.15</time>etc...</li>
    <li><time>2014.1.19</time>etc...</li>
  </ul>
</section>

<section class="abs social">
  <h3>SOCIAL</h3>
  <div class="social-box">
    <div class="page-head"><i></i><div><b>Salon</b><small>銀座ヘアサロン</small></div></div>
    <p class="post">2014年1月15日<br>銀座の店舗で新作スタイルの撮影を行いました。スタイリスト一同、新しいシーズンに向けて準備を進めています。ぜひご来店ください。</p>
    <div class="post-photo" role="img" aria-label="Stylist working with a guest in the salon"></div>
  </div>
</section>

<footer class="abs footer">
  <h2>SALON INFORMATION</h2>
  <div class="abs f-info">
    <h4>店舗情報</h4>
    <p>東京都中央区銀座0-0-0 ルミエール銀座ビル5階<br>03-0000-1234</p>
    <h4>営業時間</h4>
    <table><tr><td>月－金</td><td>11:00-21:00</td></tr><tr><td>土</td><td>10:00-20:00</td></tr><tr><td>日・祝</td><td>10:00-19:00</td></tr></table>
    <h4>最寄駅</h4>
    <p>銀座一丁目駅 徒歩2分<br>有楽町駅 徒歩5分</p>
  </div>
  <div class="abs f-btns"><span class="gold">オンライン予約</span><span>よくある質問</span><span>お問い合わせ</span></div>
  <div class="abs f-logo"><i></i>Salon</div>
  <div class="abs f-bottom"><span>よくある質問</span><span>お問い合わせ</span><span>会社概要</span><span>採用情報</span></div>
</footer>

</body>
</html>
```